Corvell Climate Job Add

We need a flashy ad we can post around our marketplace to attract new talent and employee. Our website has our company theme https://corvellclimate.ca/

Target Market(s)

HVAC, Refrigeration, Trades

Industry/Entity Type

Trades

Requirements
Must have
• a few key phrases such as "Paying above industry standard" and "No on-call requirements"

```html
<!DOCTYPE html>
<html lang="en">
<head>
<meta charset="UTF-8">
<title>Corvell Climate – We Are Hiring</title>
<link href="https://fonts.googleapis.com/css2?family=Racing+Sans+One&family=Roboto:wght@400;700&family=Montserrat:wght@400&family=Oswald:wght@600&display=swap" rel="stylesheet">
<style>
  :root {
    --blue: #0a6fc6;
    --orange: #f05a22;
    --ink: #2b2b2b;
    --black: #111111;
    --white: #ffffff;
    --rule: #d9d9d9;
    --olive: #7b8a5c;
    --belt: #e8b33a;
  }
  * { margin: 0; padding: 0; box-sizing: border-box; }
  html, body { width: 1200px; height: 1200px; overflow: hidden; background: var(--white); }
  .ad {
    position: relative;
    width: 1200px;
    height: 1200px;
    background: var(--white);
    font-family: "Roboto", Arial, sans-serif;
  }
  .brand {
    position: absolute;
    left: 56px;
    top: 150px;
    display: flex;
    align-items: center;
    gap: 14px;
  }
  .brand-dot {
    width: 42px; height: 42px;
    border-radius: 50%;
    background: var(--orange);
  }
  .brand-name {
    font-family: "Roboto", Arial, sans-serif;
    font-weight: 700;
    font-size: 38px;
    color: var(--blue);
    white-space: nowrap;
  }
  .headline {
    position: absolute;
    right: 78px;
    top: 86px;
    text-align: right;
    font-family: "Racing Sans One", "Arial Black", sans-serif;
    line-height: 1;
  }
  .headline-top {
    display: block;
    font-size: 92px;
    color: var(--ink);
    letter-spacing: 2px;
  }
  .headline-main {
    display: block;
    font-size: 122px;
    color: var(--orange);
    margin-top: 8px;
    letter-spacing: 1px;
  }
  .benefits-band {
    position: absolute;
    left: 381px;
    top: 340px;
    width: 819px;
    height: 392px;
    background: var(--blue);
  }
  .band-edge {
    position: absolute;
    left: 381px;
    top: 731px;
  }
  .benefit {
    position: absolute;
    right: 229px;
    text-align: right;
    color: var(--white);
    font-size: 36px;
    line-height: 47px;
  }
  .benefit-pay { top: 390px; }
  .benefit-oncall { top: 558px; }
  .benefit-icon {
    position: absolute;
    left: 1006px;
    width: 120px;
    height: 120px;
  }
  .benefit-icon.pay { top: 388px; }
  .benefit-icon.oncall { top: 555px; }
  .photo {
    position: absolute;
    left: 20px;
    top: 297px;
    width: 590px;
    height: 890px;
    border-radius: 280px 280px 0 0;
    background: linear-gradient(180deg, #f27a45 0%, #c9a58a 30%, var(--olive) 62%, var(--belt) 85%, var(--olive) 100%);
  }
  .join {
    position: absolute;
    right: 74px;
    top: 840px;
    font-family: "Montserrat", Arial, sans-serif;
    font-weight: 400;
    font-size: 33px;
    letter-spacing: 2px;
    color: var(--ink);
  }
  .apply {
    position: absolute;
    left: 555px;
    top: 903px;
    width: 599px;
    height: 117px;
    border: 3px solid var(--blue);
    border-radius: 60px;
  }
  .apply-circle {
    position: absolute;
    left: -3px;
    top: -3px;
    width: 120px;
    height: 117px;
    border-radius: 50%;
    background: var(--blue);
    display: flex;
    align-items: center;
    justify-content: center;
  }
  .apply-label {
    position: absolute;
    left: 166px;
    top: 6px;
    font-family: "Oswald", "Arial Narrow", sans-serif;
    font-weight: 600;
    font-size: 74px;
    line-height: 1.3;
    color: var(--orange);
    letter-spacing: 1px;
  }
  .divider {
    position: absolute;
    left: 431px;
    top: 1068px;
    width: 695px;
    height: 2px;
    background: var(--rule);
  }
  .contact {
    position: absolute;
    right: 74px;
    top: 1086px;
    display: flex;
    align-items: center;
    gap: 26px;
  }
  .contact-number {
    font-family: "Roboto", Arial, sans-serif;
    font-weight: 700;
    font-size: 58px;
    color: var(--black);
    letter-spacing: 1px;
  }
  .footer-bar {
    position: absolute;
    left: 0;
    bottom: 0;
    width: 1200px;
    height: 12px;
    background: var(--blue);
  }
</style>
</head>
<body>
<main class="ad">
  <div class="brand">
    <span class="brand-dot"></span>
    <span class="brand-name">Corvell Climate</span>
  </div>

  <h1 class="headline">
    <span class="headline-top">WE ARE</span>
    <span class="headline-main">HIRING!</span>
  </h1>

  <div class="benefits-band"></div>
  <svg class="band-edge" width="819" height="12" viewBox="0 0 819 12">
    <defs>
      <pattern id="teeth" width="20" height="12" patternUnits="userSpaceOnUse">
        <polygon points="0,0 20,0 10,12" fill="#0a6fc6"/>
      </pattern>
    </defs>
    <rect x="0" y="0" width="819" height="12" fill="url(#teeth)"/>
  </svg>

  <p class="benefit benefit-pay">Paying above<br>industry standard</p>
  <svg class="benefit-icon pay" viewBox="0 0 120 120" aria-hidden="true">
    <g fill="#ffffff">
      <circle cx="60" cy="60" r="50"/>
      <g id="tooth"><rect x="53" y="2" width="14" height="14" rx="2"/></g>
      <use href="#tooth" transform="rotate(36 60 60)"/>
      <use href="#tooth" transform="rotate(72 60 60)"/>
      <use href="#tooth" transform="rotate(108 60 60)"/>
      <use href="#tooth" transform="rotate(144 60 60)"/>
      <use href="#tooth" transform="rotate(180 60 60)"/>
      <use href="#tooth" transform="rotate(216 60 60)"/>
      <use href="#tooth" transform="rotate(252 60 60)"/>
      <use href="#tooth" transform="rotate(288 60 60)"/>
      <use href="#tooth" transform="rotate(324 60 60)"/>
    </g>
    <rect x="40" y="40" width="40" height="24" rx="3" fill="#f05a22"/>
    <circle cx="60" cy="52" r="6" fill="#ffffff"/>
    <path d="M34 74 h20 l14 6 h18 v8 h-52 z" fill="#f05a22"/>
    <rect x="28" y="34" width="10" height="14" fill="#f05a22"/>
  </svg>

  <p class="benefit benefit-oncall">No on-call<br>requirements</p>
  <svg class="benefit-icon oncall" viewBox="0 0 120 120" aria-hidden="true">
    <g fill="#ffffff">
      <circle cx="60" cy="60" r="50"/>
      <use href="#tooth"/>
      <use href="#tooth" transform="rotate(36 60 60)"/>
      <use href="#tooth" transform="rotate(72 60 60)"/>
      <use href="#tooth" transform="rotate(108 60 60)"/>
      <use href="#tooth" transform="rotate(144 60 60)"/>
      <use href="#tooth" transform="rotate(180 60 60)"/>
      <use href="#tooth" transform="rotate(216 60 60)"/>
      <use href="#tooth" transform="rotate(252 60 60)"/>
      <use href="#tooth" transform="rotate(288 60 60)"/>
      <use href="#tooth" transform="rotate(324 60 60)"/>
    </g>
    <rect x="62" y="30" width="30" height="24" rx="3" fill="#f05a22"/>
    <rect x="69" y="37" width="16" height="3" fill="#ffffff"/>
    <rect x="69" y="44" width="12" height="3" fill="#ffffff"/>
    <path d="M34 40 l10 -6 l8 14 l-7 5 q4 12 16 18 l5 -7 l14 8 l-6 10 q-30 2 -40 -42 z" fill="#f05a22"/>
  </svg>

  <div class="photo" role="img" aria-label="Photo of a smiling bearded tradesman in olive coveralls and a yellow tool belt, gesturing toward the benefits, in front of a large orange brand graphic"></div>

  <p class="join">JOIN OUR TEAM</p>

  <div class="apply">
    <span class="apply-circle">
      <svg width="54" height="54" viewBox="0 0 54 54" aria-hidden="true">
        <path d="M46 6 L8 22 L24 27 L10 44 L16 49 L30 32 L34 48 Z" fill="#ffffff"/>
      </svg>
    </span>
    <span class="apply-label">APPLY NOW</span>
  </div>

  <div class="divider"></div>

  <div class="contact">
    <svg width="48" height="48" viewBox="0 0 24 24" aria-hidden="true">
      <path d="M6.6 10.8a15.1 15.1 0 0 0 6.6 6.6l2.2-2.2a1 1 0 0 1 1-.25 11.4 11.4 0 0 0 3.6.57 1 1 0 0 1 1 1V20a1 1 0 0 1-1 1A17 17 0 0 1 3 4a1 1 0 0 1 1-1h3.5a1 1 0 0 1 1 1c0 1.25.2 2.45.57 3.6a1 1 0 0 1-.25 1z" fill="#f05a22"/>
    </svg>
    <span class="contact-number">(403) 555-0187</span>
  </div>

  <div class="footer-bar"></div>
</main>
</body>
</html>
```